Enhance the web site presence of KRU Global Limited

Upgrade the current web site www.krucircuit-example.com to share with the audience our current plan and future developments of our company. I have created a worksheet which shows all the pages that I like to have. The home page in English, Japanese and Chinese is hyperlinked to the various pages. Under the product, we should allow the user to select "single sided PCB or double sided PCB". The translation of the contents of the pages with Japanese is not complete but the English and Chinese are complete. You can download the briefing and photos in the dropbox files below;

https://www.filebinvault-example.com/sh/x7k2mq9plw4rt8a/BBQZ_Hn462UdgnRtYmXzzYfLb?dl=0

Target Market(s)

Electronic companies

Industry/Entity Type

Electronic

Coding

Coded - Design and coding required

Number of Pages Required

5+ page

Font styles to use
Sans Serif

Colors
00a990
0353a1
33b8a4

Requirements
Must have
• Get a sense of confidence on our company's integrity and capability to deliver the highest quality PCBs with the most competitive prices and best services. A sense of elegance is essential as we DON'T treat profits as the number one goal. Our number goal is to do the RIGHT things right. Having a mixture of our company photos will be appropriate.

```html
<!DOCTYPE html>
<html lang="en">
<head>
<meta charset="utf-8">
<title>Our Facility – KRU Global Limited</title>
<link href="https://fonts.googleapis.com/css2?family=Poppins:wght@300;400;500;600;700&display=swap" rel="stylesheet">
<style>
  :root{
    --teal:#33b8a4;
    --teal-deep:#00a990;
    --blue:#0353a1;
    --ink:#1c1c1c;
    --body:#555a60;
    --rule:#e3e3e3;
    --footer-muted:#8fb0d8;
  }
  *{margin:0;padding:0;box-sizing:border-box}
  html,body{width:1118px;height:1200px;overflow:hidden;background:#fff}
  body{position:relative;font-family:"Poppins",sans-serif;color:var(--body)}
  .abs{position:absolute}

  /* header */
  .brand{left:83px;top:26px;font-size:30px;font-weight:700;color:#1f5e38;letter-spacing:1px;line-height:36px}
  .contact{top:33px;font-size:12px;color:#333;display:flex;align-items:center;gap:8px;line-height:16px;white-space:nowrap}
  .contact svg{flex:none}
  .phone{left:572px}
  .email{left:732px}
  .divider{left:710px;top:24px;width:1px;height:35px;background:var(--rule)}
  .lang{left:965px;top:28px;display:flex;align-items:center;gap:8px;font-size:11.5px;color:#333}
  .flag{width:26px;height:26px;border-radius:50%;background:linear-gradient(180deg,#3a4c8f 0 45%,#e3e3ea 45% 55%,#c8303a 55% 100%);box-shadow:0 2px 4px rgba(0,0,0,.2)}

  /* hero */
  .hero{left:0;top:102px;width:1118px;height:376px;background:linear-gradient(160deg,#cfd0cc 0%,#b9bbb6 45%,#8c8f8c 80%,#5c605c 100%)}
  .hero-shade{left:0;top:102px;width:1118px;height:376px;background:rgba(40,40,40,.12)}
  .hero-curve{left:0;top:400px}
  .hero-title{left:0;width:1118px;top:226px;text-align:center;font-size:43px;font-weight:700;color:#fff;line-height:56px}
  .crumbs{left:0;width:1118px;top:292px;display:flex;justify-content:center;gap:14px;font-size:15px;font-weight:500;color:#fff;align-items:center}

  /* nav */
  .nav{left:83px;top:83px;width:952px;height:48px;background:var(--teal)}
  .nav a{position:absolute;top:0;line-height:48px;font-size:11.6px;color:#fff;text-decoration:none;text-transform:uppercase;font-weight:500}
  .nav .active::before{content:"";position:absolute;left:-3px;right:-3px;top:0;height:2px;background:#fff}
  .login{left:899px;top:83px;width:136px;height:48px;background:var(--teal-deep);display:flex;align-items:center;justify-content:center;gap:8px;color:#fff;font-size:11.6px;font-weight:600;text-transform:uppercase}

  /* gallery */
  .photo{position:absolute}
  .photo-corridor{left:83px;top:604px;width:158px;height:178px;background:linear-gradient(180deg,#e9e6cf 0%,#d3c9a5 55%,#2f8a5a 100%)}
  .photo-machine{left:310px;top:538px;width:158px;height:186px;background:linear-gradient(180deg,#f0f0ee 0%,#dcdede 60%,#3aa05a 100%)}
  .photo-operator{left:223px;top:664px;width:165px;height:233px;border:4px solid #fff;background:linear-gradient(180deg,#e8ecee 0%,#8a92d6 45%,#c7c9cb 75%,#2c9a58 100%);box-shadow:0 14px 28px rgba(0,0,0,.16)}

  /* copy */
  .eyebrow{left:569px;top:563px;font-size:14px;color:var(--teal);font-weight:500;letter-spacing:.3px}
  .headline{left:569px;top:584px;font-size:26px;font-weight:600;color:var(--ink);line-height:34px}
  .rule{left:569px;top:633px;width:33px;height:1px;background:#ccc}
  .copy{left:569px;width:465px;font-size:12px;line-height:23.2px;font-weight:300;color:var(--body);text-align:justify}
  .copy-1{top:649px}
  .copy-2{top:710px}

  /* footer */
  .footer{left:0;top:990px;width:1118px;height:210px;background:var(--blue)}
  .footer-brand{left:82px;top:1042px;font-size:30px;font-weight:700;color:#fff;letter-spacing:1px;line-height:36px}
  .footer-nav{top:1054px;left:426px;width:609px;display:flex;justify-content:space-between;font-size:11.6px;color:#fff;font-weight:500;text-transform:uppercase}
  .footer-rule{left:82px;top:1136px;width:952px;height:1px;background:rgba(255,255,255,.18)}
  .copyright{left:0;width:1118px;top:1161px;text-align:center;font-size:11px;color:var(--footer-muted);text-transform:uppercase}
  .to-top{left:1056px;top:1119px;width:34px;height:34px;border-radius:50%;background:#fff;display:flex;align-items:center;justify-content:center;box-shadow:0 2px 6px rgba(0,0,0,.2)}
</style>
</head>
<body>

<div class="abs brand">KRU</div>

<div class="abs contact phone">
  <svg width="14" height="14" viewBox="0 0 24 24"><path fill="#33b8a4" d="M6.6 10.8a15.1 15.1 0 0 0 6.6 6.6l2.2-2.2c.3-.3.7-.4 1-.2 1.1.4 2.3.6 3.6.6.6 0 1 .4 1 1V20c0 .6-.4 1-1 1A17 17 0 0 1 3 4c0-.6.4-1 1-1h3.5c.6 0 1 .4 1 1 0 1.3.2 2.5.6 3.6.1.3 0 .7-.2 1z"/></svg>
  <span>(852) 2400 5610</span>
</div>
<div class="abs divider"></div>
<div class="abs contact email">
  <svg width="14" height="11" viewBox="0 0 24 18"><path fill="#33b8a4" d="M0 2 12 10 24 2V0H0zM0 5v13h24V5l-12 8z"/></svg>
  <span>sales@krucircuit-example.com</span>
</div>
<div class="abs lang">
  <div class="flag" role="img" aria-label="English language flag"></div>
  <span>ENG</span>
  <svg width="8" height="6" viewBox="0 0 10 6"><path d="M1 1l4 4 4-4" fill="none" stroke="#333" stroke-width="1.5"/></svg>
</div>

<div class="abs hero" role="img" aria-label="Automated PCB production machines on the factory floor"></div>
<div class="abs hero-shade"></div>
<svg class="abs hero-curve" width="1118" height="80" viewBox="0 0 1118 80">
  <path d="M0 77 Q560 -22 1118 73 L1118 80 L0 80 Z" fill="#fff"/>
</svg>
<div class="abs hero-title">Our Facility</div>
<div class="abs crumbs">
  <span>Home</span>
  <svg width="12" height="10" viewBox="0 0 12 10"><path d="M1 1l4 4-4 4M6 1l4 4-4 4" fill="none" stroke="#fff" stroke-width="1.4"/></svg>
  <span>Our Facilities</span>
</div>

<nav class="abs nav">
  <a style="left:30px">Home</a>
  <a style="left:97px">Products</a>
  <a class="active" style="left:191px">Our Facilities</a>
  <a style="left:306px">Customers</a>
  <a style="left:408px">News</a>
  <a style="left:477px">Quotes</a>
  <a style="left:555px">Contact Us</a>
</nav>
<div class="abs login">
  <svg width="14" height="15" viewBox="0 0 14 15"><circle cx="7" cy="4" r="3.6" fill="#fff"/><path d="M0 15c0-4 3-6.5 7-6.5s7 2.5 7 6.5z" fill="#fff"/></svg>
  <span>User Login</span>
</div>

<div class="photo photo-corridor" role="img" aria-label="Clean-room corridor with green floor"></div>
<div class="photo photo-machine" role="img" aria-label="White automated inspection cabinets"></div>
<div class="photo photo-operator" role="img" aria-label="Operator in uniform working at an automated machine"></div>

<div class="abs eyebrow">MAINTAINING</div>
<h1 class="abs headline">A Highly Automated</h1>
<div class="abs rule"></div>
<p class="abs copy copy-1">Maintaining a highly automated factory is the only way to ensure consistent product and long term competitiveefficiency.</p>
<p class="abs copy copy-2">From 2015 to 2017, KRU invested over US$3.5 million in automating our production and quality control process and enhancing our environmental processing facility.&nbsp; We will spend a further US$1.5 million in 2018 to continue our improvement process to ensure we are one of the most efficient and highest quality single sided PCB manufacturers in Asia. By the end of 2018, 100% of our PCBs will be inspected by AVI before they are delivered to our customers.</p>

<footer class="abs footer"></footer>
<div class="abs footer-brand">KRU</div>
<div class="abs footer-nav">
  <span>Home</span><span>Products</span><span>Our Facilities</span><span>Customers</span><span>News</span><span>Quotes</span><span>Contact Us</span>
</div>
<div class="abs footer-rule"></div>
<div class="abs copyright">Copyright © 2018, KRU Global Limited. All Rights Reserved</div>
<div class="abs to-top">
  <svg width="10" height="14" viewBox="0 0 10 14"><path d="M5 13V1M1 5l4-4 4 4" fill="none" stroke="#222" stroke-width="1.2"/></svg>
</div>

</body>
</html>
```